Business Cards + Flyer + Letterhead for Care Recruitment Agency

We are a recruitment agency for the health & care sector. We need designs made for business cards, A5 double-sided flyer, and a letterhead template.

Our branding message is professionalism, care, compassion, expertise. We are experts in recruitment for the care & health industry.

Our logo source files and colours are here - https://www.fileporta.net/sh/qrvn82lopx4kdte/BBBgKy8LMQ27uTnPwZxHcVobsa?dl=0

For the business card, I have attached an example we like. We want a vertical business card design, something very similar to the example given. The design should match our logo in terms of brand colors. On one side should be our logo, our website (www.hollowmere.co.uk) and Care Recruitment Specialists written somewhere visible that fits, between our logo and the website at the bottom. On the other side should be our details.

Details on the front:

Logo with slogan
Care Recruitment Specialists
www.hollowmere.co.uk

Details on the back:

Tobias Orlund
Managing Director

Pellam House, 31-39 Larkfield St, Birmingham, B4 7QD
07612 495371
tobias@hollowmere.co.uk
www.hollowmere.co.uk

Marnie Holloway
Business Development Director

07831 204968
marnie@hollowmere.co.uk
www.hollowmere.co.uk

For the A5 flyer, I have attached some pictures we've used for the website, which could be used for the flyer as well. To get a better idea of our branding, please visit our website - https://hollowmere.co.uk/

The text for the flyer is also attached.

Finally, the letterhead template should be a docx template with our logo and our identifiable branding (the same shapes and matching colours you will come up with for the business cards and flyer).

```html
<!DOCTYPE html>
<html lang="en">
<head>
<meta charset="utf-8">
<title>Hollowmere Stationery</title>
<link rel="stylesheet" href="https://fonts.googleapis.com/css2?family=Lato:wght@400&family=Montserrat:wght@500;700&family=Poppins:wght@400;800&display=swap">
<style>
  :root{
    --navy:#0f2350;
    --navy-deep:#13306b;
    --blue:#1a6dff;
    --cyan:#00cbff;
    --ink:#1d1d1d;
    --black:#1b1b1b;
    --board:#cfcfd1;
    --white:#ffffff;
  }
  *{margin:0;padding:0;box-sizing:border-box}
  html,body{width:1200px;height:906px;overflow:hidden}
  body{background:var(--board);position:relative;font-family:'Lato',sans-serif}

  .top-bars{position:absolute;left:0;top:0;width:100%;display:flex;justify-content:space-between}
  .top-bars span{display:block;background:var(--cyan)}
  .top-bars span.mid{background:var(--navy)}

  /* ---------- Letterhead ---------- */
  .letterhead{position:absolute;left:50px;top:49px;width:568px;height:803px;background:var(--white);overflow:hidden}
  .letterhead .top-bars span{height:8px;width:183px}
  .letterhead .top-bars span.mid{width:186px}
  .lh-brand{position:absolute;left:0;top:50px;width:100%;display:flex;justify-content:center;align-items:center;gap:12px}
  .brand-dot{border-radius:50%;background:var(--blue);flex:none}
  .lh-brand .brand-dot{width:40px;height:40px}
  .lh-brand .brand-name{font-family:'Montserrat',sans-serif;font-weight:700;font-size:24px;letter-spacing:3px;color:var(--navy-deep)}

  .lh-text{position:absolute;left:53px;width:462px;font-size:12px;line-height:14.7px;color:var(--ink)}
  .lh-recipient{top:165px}
  .lh-address{top:194px;display:flex;justify-content:space-between}
  .lh-body{top:230px}
  .lh-body p{text-align:justify;margin-bottom:14.7px}
  .lh-regards{top:555px}
  .lh-signature{position:absolute;left:35px;top:580px;width:135px;height:52px;background:#f1f1f3;border-radius:4px}
  .lh-signoff{top:643px}

  .lh-footer{position:absolute;left:0;bottom:0;width:568px;height:81px;background:var(--navy)}
  .lh-footer .end-art{position:absolute;top:0;height:81px;width:112px;background:linear-gradient(90deg,var(--cyan),var(--blue))}
  .lh-footer .end-art.left{left:0}
  .lh-footer .end-art.right{right:0;background:linear-gradient(90deg,var(--blue),var(--cyan))}
  .lh-footer .contact-panel{position:absolute;left:112px;top:0;width:344px;height:81px;background:var(--black)}
  .lh-contact{position:absolute;font-family:'Montserrat',sans-serif;font-weight:500;font-size:9.5px;color:var(--white);display:flex;align-items:center;gap:6px;white-space:nowrap}
  .lh-contact svg{width:12px;height:12px;flex:none}

  /* ---------- Business cards ---------- */
  .card{position:absolute;width:213px;background:var(--white);overflow:hidden}
  .card .top-bars span{height:4px;width:68px}
  .card .top-bars span.mid{width:72px}
  .card-art{position:absolute;left:0;width:213px;background:linear-gradient(135deg,var(--cyan) 0%,var(--blue) 100%)}
  .card-panel{position:absolute;left:0;bottom:0;width:213px;background:var(--navy)}

  .card-front{left:675px;top:49px;height:371px}
  .card-front .card-art{top:165px;height:142px}
  .card-front .card-panel{height:59px}
  .cf-dot{position:absolute;left:84px;top:54px;width:44px;height:44px}
  .cf-name{position:absolute;left:0;top:117px;width:100%;text-align:center;font-family:'Montserrat',sans-serif;font-weight:700;font-size:18px;letter-spacing:2px;color:var(--navy-deep)}
  .cf-tagline{position:absolute;left:0;top:138px;width:100%;text-align:center;font-family:'Montserrat',sans-serif;font-weight:500;font-size:7.5px;letter-spacing:1.6px;color:var(--navy)}
  .cf-web{position:absolute;left:0;top:341px;width:100%;text-align:center;font-family:'Poppins',sans-serif;font-size:7px;letter-spacing:3px;color:var(--white)}

  .card-back{top:477px;height:372px}
  .card-back .card-art{top:90px;height:141px}
  .card-back .card-panel{height:136px}
  .card-back.md{left:675px}
  .card-back.bdd{left:933px}
  .cb-name{position:absolute;left:0;width:100%;text-align:center;font-family:'Poppins',sans-serif;font-weight:800;font-size:17px;color:var(--blue);line-height:1}
  .cb-role{position:absolute;left:0;width:100%;text-align:center;font-family:'Poppins',sans-serif;font-size:7px;color:var(--navy);line-height:1}
  .md .cb-name{top:58px}.md .cb-role{top:76px}
  .bdd .cb-name{top:47px}.bdd .cb-role{top:65px}
  .cb-details{position:absolute;left:20px;top:265px;width:190px;list-style:none;font-family:'Poppins',sans-serif;font-size:9.6px;line-height:11px;color:var(--white)}
  .cb-details li{display:flex;align-items:flex-start;gap:6px;margin-bottom:10px}
  .cb-details li.addr{margin-bottom:7px}
  .cb-details svg{width:14px;height:14px;flex:none}
</style>
</head>
<body>

<svg width="0" height="0" style="position:absolute" aria-hidden="true">
  <defs>
    <symbol id="ico-phone" viewBox="0 0 14 14"><circle cx="7" cy="7" r="6.2" fill="none" stroke="#1a6dff" stroke-width="1"/><path d="M4.6 4.1l1.2-.3.7 1.6-.8.6c.4.9 1 1.5 1.9 1.9l.6-.8 1.6.7-.3 1.2c-2.7.2-5.1-2.2-4.9-4.9z" fill="#1a6dff"/></symbol>
    <symbol id="ico-pin" viewBox="0 0 14 14"><circle cx="7" cy="7" r="6.2" fill="none" stroke="#1a6dff" stroke-width="1"/><path d="M7 3.2a2.6 2.6 0 0 0-2.6 2.6C4.4 7.8 7 10.8 7 10.8s2.6-3 2.6-5A2.6 2.6 0 0 0 7 3.2z" fill="none" stroke="#1a6dff" stroke-width="1"/><circle cx="7" cy="5.8" r=".9" fill="#1a6dff"/></symbol>
    <symbol id="ico-mail" viewBox="0 0 14 14"><circle cx="7" cy="7" r="6.2" fill="none" stroke="#1a6dff" stroke-width="1"/><rect x="3.8" y="4.8" width="6.4" height="4.4" fill="none" stroke="#1a6dff" stroke-width=".9"/><path d="M3.8 4.8L7 7.3l3.2-2.5" fill="none" stroke="#1a6dff" stroke-width=".9"/></symbol>
    <symbol id="ico-web" viewBox="0 0 14 14"><circle cx="7" cy="7" r="6.2" fill="none" stroke="#1a6dff" stroke-width="1"/><circle cx="7" cy="7" r="3.4" fill="none" stroke="#1a6dff" stroke-width=".8"/><ellipse cx="7" cy="7" rx="1.4" ry="3.4" fill="none" stroke="#1a6dff" stroke-width=".8"/><path d="M3.6 7h6.8" stroke="#1a6dff" stroke-width=".8"/></symbol>
    <symbol id="ico-phone-w" viewBox="0 0 14 14"><circle cx="7" cy="7" r="6.5" fill="#fff"/><rect x="5" y="3.3" width="4" height="7.4" rx=".8" fill="none" stroke="#1a6dff" stroke-width=".9"/></symbol>
    <symbol id="ico-pin-w" viewBox="0 0 14 14"><circle cx="7" cy="7" r="6.5" fill="#fff"/><path d="M7 3.2a2.6 2.6 0 0 0-2.6 2.6C4.4 7.8 7 10.8 7 10.8s2.6-3 2.6-5A2.6 2.6 0 0 0 7 3.2z" fill="#1a6dff"/><circle cx="7" cy="5.8" r=".9" fill="#fff"/></symbol>
    <symbol id="ico-mail-w" viewBox="0 0 14 14"><circle cx="7" cy="7" r="6.5" fill="#fff"/><rect x="3.8" y="4.8" width="6.4" height="4.4" fill="#1a6dff"/><path d="M3.8 4.8L7 7.3l3.2-2.5" fill="none" stroke="#fff" stroke-width=".8"/></symbol>
    <symbol id="ico-web-w" viewBox="0 0 14 14"><circle cx="7" cy="7" r="6.5" fill="#fff"/><circle cx="7" cy="7" r="3.6" fill="none" stroke="#1a6dff" stroke-width=".8"/><ellipse cx="7" cy="7" rx="1.4" ry="3.6" fill="none" stroke="#1a6dff" stroke-width=".8"/><path d="M3.4 7h7.2" stroke="#1a6dff" stroke-width=".8"/></symbol>
  </defs>
</svg>

<!-- Letterhead -->
<section class="letterhead">
  <div class="top-bars"><span></span><span class="mid"></span><span></span></div>

  <div class="lh-brand">
    <span class="brand-dot"></span>
    <span class="brand-name">HOLLOWMERE</span>
  </div>

  <div class="lh-text lh-recipient">Your Name Here</div>
  <div class="lh-text lh-address"><span>Address</span><span>Date : 17th September, 2020</span></div>

  <div class="lh-text lh-body">
    <p>Lorem Ipsum is simply dummy text of the printing and typesetting industry. Lorem Ipsum has been the industry's standard dummy text ever since the 1500s, when an unknown printer took a galley of type and scrambled it to make a type specimen book. It has survived not only five centuries, but also the leap into electronic typesetting, remaining essentially unchanged. It was popularised in the 1960s with the release of Tessprint sheets containing Lorem Ipsum passages, and more recently with desktop publishing software like Quillset Pagewright including versions of Lorem Ipsum.</p>
    <p>Lorem Ipsum is simply dummy text of the printing and typesetting industry. Lorem Ipsum has been the industry's standard dummy text ever since the 1500s, when an unknown printer took a galley of type and scrambled it to make a type specimen book. but also the leap into electronic typesetting, remaining essentially unchanged. It was popularised in the 1960s with the release of Tessprint sheets containing Lorem Ipsum passages, and more recently with desktop publishing software like Quillset Pagewright including versions of Lorem Ipsum.</p>
    <p>It has survived not only five centuries, but also the leap into electronic typesetting, remaining essentially unchanged. It was popularised in the 1960s with the release of Tessprint sheets containing Lorem Ipsum passages, and more recently with desktop publishing software like Quillset Pagewright including versions of Lorem Ipsum.</p>
  </div>

  <div class="lh-text lh-regards">Regards,</div>
  <div class="lh-signature" role="img" aria-label="Handwritten signature of the sender"></div>
  <div class="lh-text lh-signoff">Your Name Here<br>Designation Here</div>

  <div class="lh-footer">
    <div class="end-art left" role="img" aria-label="Decorative brand stripes in cyan and blue"></div>
    <div class="contact-panel"></div>
    <div class="end-art right" role="img" aria-label="Decorative brand stripes in blue and cyan"></div>
  </div>
  <div class="lh-contact" style="left:151px;top:749px"><svg><use href="#ico-phone-w"/></svg>12345 54321</div>
  <div class="lh-contact" style="left:151px;top:769px"><svg><use href="#ico-pin-w"/></svg>lorem ipsum dolor sit amet</div>
  <div class="lh-contact" style="left:308px;top:747px"><svg><use href="#ico-mail-w"/></svg>loremipsum@postbox.co.uk</div>
  <div class="lh-contact" style="left:308px;top:767px"><svg><use href="#ico-web-w"/></svg>www.hollowmere.co.uk</div>
</section>

<!-- Business card front -->
<section class="card card-front">
  <div class="top-bars"><span></span><span class="mid"></span><span></span></div>
  <span class="brand-dot cf-dot"></span>
  <div class="cf-name">HOLLOWMERE</div>
  <div class="cf-tagline">CARE RECRUITMENT SPECIALISTS</div>
  <div class="card-art" role="img" aria-label="Decorative brand graphic in cyan to blue"></div>
  <div class="card-panel"></div>
  <div class="cf-web">WWW.HOLLOWMERE.CO.UK</div>
</section>

<!-- Business card back: Managing Director -->
<section class="card card-back md">
  <div class="top-bars"><span></span><span class="mid"></span><span></span></div>
  <h2 class="cb-name">TOBIAS ORLUND</h2>
  <p class="cb-role">MANAGING DIRECTOR</p>
  <div class="card-art" role="img" aria-label="Decorative brand graphic in cyan to blue"></div>
  <div class="card-panel"></div>
  <ul class="cb-details">
    <li><svg><use href="#ico-phone"/></svg>07612 495371</li>
    <li class="addr"><svg><use href="#ico-pin"/></svg>Pellam House, 31-39 Larkfield St,<br>Birmingham, B4 7QD</li>
    <li><svg><use href="#ico-mail"/></svg>tobias@hollowmere.co.uk</li>
    <li><svg><use href="#ico-web"/></svg>www.hollowmere.co.uk</li>
  </ul>
</section>

<!-- Business card back: Business Development Director -->
<section class="card card-back bdd">
  <div class="top-bars"><span></span><span class="mid"></span><span></span></div>
  <h2 class="cb-name">MARNIE HOLLOWAY</h2>
  <p class="cb-role">BUSINESS DEVELOPMENT DIRECTOR</p>
  <div class="card-art" role="img" aria-label="Decorative brand graphic in cyan to blue"></div>
  <div class="card-panel"></div>
  <ul class="cb-details">
    <li><svg><use href="#ico-phone"/></svg>07831 204968</li>
    <li class="addr"><svg><use href="#ico-pin"/></svg>Pellam House, 31-39 Larkfield St,<br>Birmingham, B4 7QD</li>
    <li><svg><use href="#ico-mail"/></svg>marnie@hollowmere.co.uk</li>
    <li><svg><use href="#ico-web"/></svg>www.hollowmere.co.uk</li>
  </ul>
</section>

</body>
</html>
```